Upmarket Bathroom and Kitchen ware supplier needs a classy business card design

We are a company based in Fiji, we sell plumbing ware (Kitchen and bathroom taps, Basins,showers, toilets etc) through up market show rooms to individuals and directly through Architects and designers of resorts and holiday houses for new builds and renovations. we are wanting to upgrade our over all look and brand. we are starting with a new logo but will be rebranding the whole business. This project is for a business card design for my management and tales team I would like it to be dark, classy and interesting

Target Market(s)

Resort directors and Management, High end holiday home owners

Contact Information for Business Card

Neil Dawson
Director
+64219473815

Colors

Designer to choose colors to be used in the design.

Requirements
Must have
• Must have an upmarket appearance I like darker charcoal shades but will be guided by the designers
• Please any catch phrases like "Crafting remarkable living rooms" this belongs tpo one of our suppliers so can not be used.
Nice to have
• Double sided, so front dedicated to logo provided and back info about the business and the person.

```html
<!DOCTYPE html>
<html lang="en">
<head>
<meta charset="UTF-8">
<title>Solace Interiors – Business Card</title>
<link rel="stylesheet" href="https://fonts.googleapis.com/css2?family=Montserrat:wght@400&family=Oswald:wght@500&display=swap">
<style>
  :root {
    --backdrop-light: #2b2b2c;
    --backdrop-dark: #0e0e0f;
    --card: #1d1d1e;
    --card-edge: #262627;
    --silver: #c8c8ca;
    --silver-soft: #a9a9ab;
  }
  * { margin: 0; padding: 0; box-sizing: border-box; }
  html, body {
    width: 1200px;
    height: 900px;
    overflow: hidden;
  }
  body {
    background: radial-gradient(ellipse at 50% 40%, var(--backdrop-light), var(--backdrop-dark) 75%);
    font-family: "Montserrat", Arial, sans-serif;
    color: var(--silver);
  }
  .card-stack {
    position: absolute;
    left: 290px;
    top: 76px;
    width: 620px;
    display: flex;
    flex-direction: column;
    gap: 40px;
  }
  .card {
    position: relative;
    width: 620px;
    height: 354px;
    background: linear-gradient(135deg, var(--card-edge), var(--card) 60%);
    box-shadow: 0 18px 40px rgba(0, 0, 0, 0.55);
  }

  /* Front */
  .brand {
    position: absolute;
    left: 0;
    right: 0;
    top: 158px;
    display: flex;
    align-items: center;
    justify-content: center;
    gap: 14px;
  }
  .brand-dot {
    width: 16px;
    height: 16px;
    border-radius: 50%;
    background: var(--silver);
  }
  .brand-name {
    font-weight: 400;
    font-size: 24px;
    line-height: 1;
    color: var(--silver);
  }

  /* Back */
  .person {
    position: absolute;
    right: 355px;
    top: 128px;
    text-align: right;
  }
  .person-name {
    font-family: "Oswald", "Arial Narrow", sans-serif;
    font-weight: 500;
    font-size: 30px;
    letter-spacing: 0.03em;
    color: var(--silver);
    line-height: 1.1;
  }
  .person-role {
    font-size: 15px;
    color: var(--silver-soft);
    margin-top: 2px;
  }
  .divider {
    position: absolute;
    left: 300px;
    top: 125px;
    width: 2px;
    height: 72px;
    background: var(--silver-soft);
  }
  .contacts {
    position: absolute;
    left: 330px;
    top: 130px;
    list-style: none;
    font-size: 16px;
    line-height: 24px;
    color: var(--silver);
  }
  .contacts li {
    display: flex;
    align-items: center;
    gap: 10px;
  }
  .contacts svg {
    width: 12px;
    height: 12px;
    fill: none;
    stroke: var(--silver);
    stroke-width: 1.6;
  }
  .address {
    position: absolute;
    left: 0;
    right: 0;
    bottom: 40px;
    text-align: center;
    font-size: 16px;
    letter-spacing: 0.02em;
    color: var(--silver-soft);
  }
</style>
</head>
<body>
  <main class="card-stack">
    <section class="card card-front">
      <div class="brand">
        <div class="brand-dot"></div>
        <div class="brand-name">Solace Interiors</div>
      </div>
    </section>

    <section class="card card-back">
      <div class="person">
        <div class="person-name">NEIL DAWSON</div>
        <div class="person-role">Director</div>
      </div>
      <div class="divider"></div>
      <ul class="contacts">
        <li>
          <svg viewBox="0 0 12 12"><path d="M3 1 L5 3.5 L4 5 Q5 7.5 7 8 L8.5 7 L11 9 L9.5 11 Q3 10 1 2.5 Z"/></svg>
          +64219473815
        </li>
        <li>
          <svg viewBox="0 0 12 12"><rect x="1" y="2.5" width="10" height="7"/><path d="M1 2.5 L6 6.5 L11 2.5"/></svg>
          info@solacehome.com
        </li>
        <li>
          <svg viewBox="0 0 12 12"><circle cx="6" cy="6" r="5"/><ellipse cx="6" cy="6" rx="2.2" ry="5"/><path d="M1 6 H11"/></svg>
          www.solacehome.com
        </li>
      </ul>
      <p class="address">1420 Silver Reef Lane Maple Grove, NJ 07840</p>
    </section>
  </main>
</body>
</html>
```